a mobile app for beauty salon professional to publish their service and customers to book service

I plan to create an iPhone app (support iPhone 6 and above) that will allow beauty salon professionals (e.g. hair stylist) to publish their service/business with address/geolocation and available time slots, manage their professional profile with photos, and service charges, allow the customers to search services based on locations, and book the service. customer can provide feedback/ratings on the professional's service. a reference website : http://mira.tovelpa.example/booking/

Target Market(s)

beauty and hair salon professionals and customers

Industry/Entity Type

Hair And Beauty

Font styles to use
Sans Serif
Script

Colors

Designer to choose colors to be used in the design.

Requirements
Must have
• === customer features
• - user/customer registration
• - customer browse nearby service using a map view
• - customer browse nearby service using a list view ordered by distance (e.g. km)
• - customer search salon service based on service category, price range, and profressional's rating
• - customer select a service with zoom in details : salon name, service offered, location/address, and a "booking" button
• - customer place booking by specifying service (e.g. simple cut, blow-dry, etc) required, time slot, preferred professional
• - customer payments (paypal/credit card)
• - customer can feedback/rate on the salon professional
• === salon professional features
• - user/professional registration
• - maintain professional profile (private/public), option to upload photos
• - a registered professional can register/maintain shop/business who by default is the owner of the shop/business
• - a shop owner can assign professionals to the shop/business (multiple professional can work in the same location/shop)
• - professional maintain their service and schedule (breaks, holidays, working hours, appointments, service rates)

```html
<!DOCTYPE html>
<html lang="en">
<head>
<meta charset="utf-8">
<title>Salon Finder – Map View</title>
<link rel="stylesheet" href="https://fonts.googleapis.com/css2?family=Montserrat:wght@400;500;600&display=swap">
<style>
  :root {
    --canvas-bg: #f4f4f6;
    --screen-bg: #ffffff;
    --brand-pink: #e8166b;
    --ink: #1d1d1f;
    --ink-soft: #55565a;
    --search-fill: #f2f2f4;
    --map-grey: #e8e7e3;
    --map-grey-light: #efeeea;
    --map-water: #b9d6f2;
    --map-park: #d3e8c4;
    --pin-stem: #5a5a5e;
    --locator: #1a73e8;
    --locator-halo: rgba(26, 115, 232, 0.18);
  }
  * { box-sizing: border-box; margin: 0; padding: 0; }
  html, body {
    width: 1200px; height: 1200px; overflow: hidden;
    background: var(--canvas-bg);
    font-family: "Montserrat", sans-serif;
    color: var(--ink);
  }
  .app-screen {
    position: absolute; left: 300px; top: 66px;
    width: 600px; height: 1067px;
    background: var(--screen-bg);
    overflow: hidden;
    border-radius: 6px;
    box-shadow: 0 10px 40px rgba(0,0,0,0.08);
  }
  .status-bar {
    position: absolute; top: 0; left: 0; right: 0; height: 36px;
    display: flex; align-items: center; justify-content: space-between;
    padding: 0 16px; font-size: 16px; font-weight: 500;
  }
  .status-left, .status-right { display: flex; align-items: center; gap: 6px; }
  .status-time { position: absolute; left: 50%; transform: translateX(-50%); font-weight: 600; }
  .top-bar {
    position: absolute; top: 44px; left: 0; right: 0; height: 92px;
    display: flex; align-items: center; padding: 0 18px; gap: 16px;
  }
  .back-button, .filter-button { width: 36px; height: 36px; flex: none; }
  .search-pill {
    flex: 1; height: 80px; border-radius: 40px;
    background: var(--search-fill);
    display: flex; flex-direction: column; justify-content: center; align-items: center;
    white-space: nowrap;
  }
  .search-query { font-size: 27px; font-weight: 500; line-height: 1.2; }
  .search-count { font-size: 17px; color: var(--ink-soft); margin-top: 4px; }
  .map-area {
    position: absolute; top: 144px; left: 0; right: 0; bottom: 0;
    background: linear-gradient(165deg,
      var(--map-grey-light) 0%,
      var(--map-grey) 28%,
      var(--map-water) 42%,
      var(--map-grey) 56%,
      var(--map-park) 70%,
      var(--map-grey) 84%,
      var(--map-grey-light) 100%);
  }
  .map-pin { position: absolute; width: 24px; height: 40px; }
  .user-locator {
    position: absolute; width: 80px; height: 80px; border-radius: 50%;
    background: var(--locator-halo);
    display: flex; align-items: center; justify-content: center;
  }
  .user-locator::after {
    content: ""; width: 20px; height: 20px; border-radius: 50%;
    background: var(--locator); border: 3px solid #fff;
  }
  .list-sheet {
    position: absolute; left: 0; right: 0; bottom: 0; height: 150px;
    background: var(--screen-bg);
    border-radius: 24px 24px 0 0;
    box-shadow: 0 -6px 20px rgba(0,0,0,0.08);
    display: flex; flex-direction: column; align-items: center; padding-top: 30px;
    color: var(--brand-pink); font-size: 22px; font-weight: 500;
  }
</style>
</head>
<body>
<main class="app-screen">
  <header class="status-bar">
    <div class="status-left">
      <svg width="22" height="14" viewBox="0 0 22 14"><rect x="0" y="10" width="3" height="4" fill="#1d1d1f"/><rect x="5" y="7" width="3" height="7" fill="#1d1d1f"/><rect x="10" y="4" width="3" height="10" fill="#1d1d1f"/><rect x="15" y="0" width="3" height="14" fill="#1d1d1f"/></svg>
      <span class="carrier">Nimbus</span>
      <svg width="18" height="14" viewBox="0 0 18 14"><path d="M1 5a11 11 0 0 1 16 0M4 8a7 7 0 0 1 10 0M7 11a3 3 0 0 1 4 0" stroke="#1d1d1f" stroke-width="2" fill="none"/></svg>
    </div>
    <span class="status-time">9:41 AM</span>
    <div class="status-right">
      <span>100%</span>
      <svg width="34" height="16" viewBox="0 0 34 16"><rect x="1" y="1" width="28" height="14" rx="3" fill="none" stroke="#1d1d1f" stroke-width="1.5"/><rect x="3" y="3" width="24" height="10" rx="1.5" fill="#1d1d1f"/><rect x="30" y="5" width="3" height="6" rx="1" fill="#1d1d1f"/></svg>
    </div>
  </header>

  <nav class="top-bar">
    <svg class="back-button" viewBox="0 0 36 36" aria-label="Back"><path d="M22 8 L12 18 L22 28" stroke="var(--brand-pink)" stroke-width="2.5" fill="none" stroke-linecap="round"/></svg>
    <div class="search-pill">
      <span class="search-query">haircut for men</span>
      <span class="search-count">Showing 280 salons in Vancouver</span>
    </div>
    <svg class="filter-button" viewBox="0 0 36 36" aria-label="Filters"><g stroke="var(--brand-pink)" stroke-width="2.5" stroke-linecap="round"><line x1="6" y1="10" x2="30" y2="10"/><line x1="10" y1="18" x2="30" y2="18"/><line x1="16" y1="26" x2="30" y2="26"/></g></svg>
  </nav>

  <section class="map-area" role="img" aria-label="Street map of downtown Vancouver with streets, neighbourhood labels, False Creek waterway and parks; pink pins mark nearby salons">
    <svg class="map-pin" style="left:120px;top:90px" viewBox="0 0 24 40"><line x1="12" y1="12" x2="12" y2="38" stroke="var(--pin-stem)" stroke-width="2"/><circle cx="12" cy="10" r="9" fill="var(--brand-pink)"/></svg>
    <svg class="map-pin" style="left:300px;top:60px" viewBox="0 0 24 40"><line x1="12" y1="12" x2="12" y2="38" stroke="var(--pin-stem)" stroke-width="2"/><circle cx="12" cy="10" r="9" fill="var(--brand-pink)"/></svg>
    <svg class="map-pin" style="left:470px;top:40px" viewBox="0 0 24 40"><line x1="12" y1="12" x2="12" y2="38" stroke="var(--pin-stem)" stroke-width="2"/><circle cx="12" cy="10" r="9" fill="var(--brand-pink)"/></svg>
    <svg class="map-pin" style="left:60px;top:220px" viewBox="0 0 24 40"><line x1="12" y1="12" x2="12" y2="38" stroke="var(--pin-stem)" stroke-width="2"/><circle cx="12" cy="10" r="9" fill="var(--brand-pink)"/></svg>
    <svg class="map-pin" style="left:210px;top:200px" viewBox="0 0 24 40"><line x1="12" y1="12" x2="12" y2="38" stroke="var(--pin-stem)" stroke-width="2"/><circle cx="12" cy="10" r="9" fill="var(--brand-pink)"/></svg>
    <svg class="map-pin" style="left:350px;top:170px" viewBox="0 0 24 40"><line x1="12" y1="12" x2="12" y2="38" stroke="var(--pin-stem)" stroke-width="2"/><circle cx="12" cy="10" r="9" fill="var(--brand-pink)"/></svg>
    <svg class="map-pin" style="left:140px;top:330px" viewBox="0 0 24 40"><line x1="12" y1="12" x2="12" y2="38" stroke="var(--pin-stem)" stroke-width="2"/><circle cx="12" cy="10" r="9" fill="var(--brand-pink)"/></svg>
    <svg class="map-pin" style="left:270px;top:300px" viewBox="0 0 24 40"><line x1="12" y1="12" x2="12" y2="38" stroke="var(--pin-stem)" stroke-width="2"/><circle cx="12" cy="10" r="9" fill="var(--brand-pink)"/></svg>
    <svg class="map-pin" style="left:500px;top:250px" viewBox="0 0 24 40"><line x1="12" y1="12" x2="12" y2="38" stroke="var(--pin-stem)" stroke-width="2"/><circle cx="12" cy="10" r="9" fill="var(--brand-pink)"/></svg>
    <svg class="map-pin" style="left:80px;top:470px" viewBox="0 0 24 40"><line x1="12" y1="12" x2="12" y2="38" stroke="var(--pin-stem)" stroke-width="2"/><circle cx="12" cy="10" r="9" fill="var(--brand-pink)"/></svg>
    <svg class="map-pin" style="left:360px;top:430px" viewBox="0 0 24 40"><line x1="12" y1="12" x2="12" y2="38" stroke="var(--pin-stem)" stroke-width="2"/><circle cx="12" cy="10" r="9" fill="var(--brand-pink)"/></svg>
    <svg class="map-pin" style="left:440px;top:470px" viewBox="0 0 24 40"><line x1="12" y1="12" x2="12" y2="38" stroke="var(--pin-stem)" stroke-width="2"/><circle cx="12" cy="10" r="9" fill="var(--brand-pink)"/></svg>
    <svg class="map-pin" style="left:530px;top:400px" viewBox="0 0 24 40"><line x1="12" y1="12" x2="12" y2="38" stroke="var(--pin-stem)" stroke-width="2"/><circle cx="12" cy="10" r="9" fill="var(--brand-pink)"/></svg>
    <svg class="map-pin" style="left:180px;top:600px" viewBox="0 0 24 40"><line x1="12" y1="12" x2="12" y2="38" stroke="var(--pin-stem)" stroke-width="2"/><circle cx="12" cy="10" r="9" fill="var(--brand-pink)"/></svg>
    <svg class="map-pin" style="left:300px;top:640px" viewBox="0 0 24 40"><line x1="12" y1="12" x2="12" y2="38" stroke="var(--pin-stem)" stroke-width="2"/><circle cx="12" cy="10" r="9" fill="var(--brand-pink)"/></svg>
    <svg class="map-pin" style="left:60px;top:700px" viewBox="0 0 24 40"><line x1="12" y1="12" x2="12" y2="38" stroke="var(--pin-stem)" stroke-width="2"/><circle cx="12" cy="10" r="9" fill="var(--brand-pink)"/></svg>
    <svg class="map-pin" style="left:520px;top:640px" viewBox="0 0 24 40"><line x1="12" y1="12" x2="12" y2="38" stroke="var(--pin-stem)" stroke-width="2"/><circle cx="12" cy="10" r="9" fill="var(--brand-pink)"/></svg>
    <div class="user-locator" style="left:400px;top:580px"></div>
  </section>

  <footer class="list-sheet">
    <svg width="28" height="18" viewBox="0 0 28 18"><path d="M4 10 L14 3 L24 10 M4 16 L14 9 L24 16" stroke="var(--brand-pink)" stroke-width="2" fill="none" stroke-linecap="round"/></svg>
    <span class="list-toggle">Show All Lists</span>
  </footer>
</main>
</body>
</html>
```